Private Investigation Business Card Design

I need a business card for a new private investigation company named Brisk Lens Inquiries. I perform mainly surveillance jobs, vehicle repossessions, document serves etc. The final design should aim for a professional look. The logo has a magnifying glass with stick man arms and legs and is in a running action to show the "BRISK" aspect of the name. If the colour scheme could remain the same as the website www.brisklensinquiries.example.au with silvers,blacks and a couple electric blue highlights.
Industry/Entity Type
Business
Contact Information for Business Card
Morgan Kilbride
Brisk Lens Inquiries
0438276104
PO Box 58, Fernvale NSW 2291
info@brisklensinquiries.example.au
www.brisklensinquiries.example.au
Look and feel
Each slider illustrates characteristics of the customer's brand and the style your logo design should communicate.

```html
<!DOCTYPE html>
<html lang="en">
<head>
<meta charset="utf-8">
<title>Brisk Lens Inquiries – Business Card</title>
<link href="https://fonts.googleapis.com/css2?family=Open+Sans:wght@400;600;700&display=swap" rel="stylesheet">
<style>
  :root {
    --stage: #2a2a2a;
    --card: #0c0c0c;
    --card-edge: #1c1c1c;
    --ink: #ffffff;
    --ink-soft: #d9d9d9;
    --rule: #e6e6e6;
  }
  * { box-sizing: border-box; margin: 0; padding: 0; }
  html, body { width: 1200px; height: 900px; overflow: hidden; }
  body {
    background: var(--stage);
    font-family: "Open Sans", Arial, sans-serif;
    color: var(--ink);
    position: relative;
  }
  .card {
    position: absolute;
    width: 640px;
    height: 340px;
    overflow: hidden;
    background: linear-gradient(135deg, var(--card-edge) 0%, var(--card) 60%);
    box-shadow: 0 14px 30px rgba(0,0,0,0.55);
  }
  .card--front { left: 280px; top: 60px; }
  .card--back  { left: 280px; top: 480px; }

  .brand {
    display: flex;
    align-items: center;
    gap: 14px;
    font-weight: 700;
    color: var(--ink);
    letter-spacing: 0.02em;
    line-height: 1;
    white-space: nowrap;
  }
  .brand__dot {
    flex: none;
    border-radius: 50%;
    background: var(--ink);
  }
  .card--front .brand {
    position: absolute;
    left: 56px;
    top: 148px;
    font-size: 40px;
  }
  .card--front .brand__dot { width: 30px; height: 30px; }

  .card--back .brand {
    position: absolute;
    left: 34px;
    top: 160px;
    font-size: 21px;
    gap: 9px;
  }
  .card--back .brand__dot { width: 16px; height: 16px; }

  .divider {
    position: absolute;
    left: 328px;
    top: 40px;
    width: 2px;
    height: 260px;
    background: var(--rule);
  }
  .contact {
    position: absolute;
    left: 348px;
    top: 44px;
    font-size: 14.5px;
    color: var(--ink-soft);
    line-height: 1.32;
  }
  .contact__first { font-size: 19px; font-weight: 700; color: var(--ink); }
  .contact__last { font-size: 14px; margin-left: 8px; margin-bottom: 4px; }
  .contact__address { margin-left: 8px; margin-bottom: 8px; }
  .contact__list { list-style: none; }
  .contact__list li {
    display: flex;
    align-items: center;
    gap: 10px;
    margin-bottom: 6px;
    white-space: nowrap;
  }
  .contact__list svg { width: 14px; height: 14px; flex: none; }
</style>
</head>
<body>
  <section class="card card--front" aria-label="Card front">
    <div class="brand"><span class="brand__dot"></span>BRISK LENS INQUIRIES</div>
  </section>

  <section class="card card--back" aria-label="Card back">
    <div class="brand"><span class="brand__dot"></span>BRISK LENS INQUIRIES</div>
    <div class="divider"></div>
    <div class="contact">
      <div class="contact__first">Morgan</div>
      <div class="contact__last">Kilbride</div>
      <div class="contact__address">Unit 9/42 Ridge Street<br>First floor</div>
      <ul class="contact__list">
        <li>
          <svg viewBox="0 0 16 16" aria-hidden="true"><path fill="#ddd" d="M3.6 1.5l2.3 2.6-1.2 1.9c.9 2 2.4 3.5 4.4 4.4l1.9-1.2 2.6 2.3-1.4 2.6C7 13.6 2.4 9 1 3z"/></svg>
          <span>0438276104</span>
        </li>
        <li>
          <svg viewBox="0 0 16 16" aria-hidden="true"><rect x="1" y="3.5" width="14" height="9.5" fill="#ddd"/><path d="M1 3.5l7 5.5 7-5.5" fill="none" stroke="#0c0c0c" stroke-width="1.2"/></svg>
          <span>PO Box 58, Fernvale NSW 2291</span>
        </li>
        <li>
          <svg viewBox="0 0 16 16" aria-hidden="true"><g fill="none" stroke="#ddd" stroke-width="1.2"><circle cx="8" cy="8" r="6.5"/><ellipse cx="8" cy="8" rx="3" ry="6.5"/><path d="M1.5 8h13M2.5 4.5h11M2.5 11.5h11"/></g></svg>
          <span>www.brisklensinquiries.example.au</span>
        </li>
        <li>
          <svg viewBox="0 0 16 16" aria-hidden="true"><text x="8" y="12.5" text-anchor="middle" font-family="Open Sans, Arial, sans-serif" font-size="14" font-weight="700" fill="#ddd">@</text></svg>
          <span>info@brisklensinquiries.example.au</span>
        </li>
      </ul>
    </div>
  </section>
</body>
</html>
```